Book Cover Design Project

NOTE. I need the design in four days of posting this!

This will be the cover of my first book, WALK THE HIGH LINE -
alchemy in the real business world. The book explains defines what Purpose and Meaning is, and how to use it in business. I have included the first chapter to provide a background.

I want the core colours to be black and white, and use the colours Violet, Cerulean Blue Extra Pale (powder blue), Cadmium Lemon (flouro yellow). I plan on using this design as the basis for future books in the WALK THE HIGH LINE series, where the yellow is carried through but the violet and blue colours changing.

This is a spiritual business book without using any spiritual language. It is strongly masculine and direct in its nature.

What I am looking for is something Remarkable that captures my reader immediately. My reader is a seeker. He/she is an entrepreneur perhaps looking to setup a new venture and looking for new and better ways of doing things, or he/she may be a small/medium business owner perhaps bored looking for more meaning in personal and business life), or the corporate person who is looking to get out and do something new. Age 35-50.
Updates

Hi I want to correct the paper size. It is "C Format" (trade paperbacks) are 135mm x 216mm (5.32" x 8.51").

Thks

Reason: A deadline has changed which means the completion of this book cover is less time-critical.

This is a business book that introduces new concepts, such as Purpose. Although it is based on spiritual principals  it is using normal business language when explaining what Purpose is, and how businesses can identify it and use it to be more successful.

If there is a border between a self-help and a business book, this book sits close to the border but markedly on the business side.

Hi I want to confirm the book size. The book size I require is the Australian C Format, which measures 153mm W x 234mm H. 

Sorry for any confusion

Reason: Hi I have extended the deadline as I want to be able to print prospective covers and see how they look like in a bookshop next to other covers.

Reason: To allow for final negotiations.

Industry/Entity Type

Business

```html
<!DOCTYPE html>
<html lang="en">
<head>
<meta charset="utf-8">
<title>Walk the High Line – Front Cover</title>
<link rel="stylesheet" href="https://fonts.googleapis.com/css2?family=Jost:ital,wght@0,300;0,400;0,700;1,800&display=swap">
<style>
  :root {
    --paper: #ffffff;
    --ink: #000000;
    --violet: #8e2a8b;
    --lemon: #fff200;
    --text-light: #ffffff;
  }
  * { margin: 0; padding: 0; box-sizing: border-box; }
  html, body {
    width: 927px;
    height: 1200px;
    overflow: hidden;
    background: var(--paper);
  }
  .artboard {
    position: relative;
    width: 927px;
    height: 1200px;
    background: var(--paper);
    font-family: "Jost", sans-serif;
  }
  .proof-label {
    position: absolute;
    left: 205px;
    top: 72px;
    font-family: "Jost", sans-serif;
    font-weight: 300;
    font-size: 36px;
    letter-spacing: 0.5px;
    color: var(--violet);
  }
  .cover-shape {
    position: absolute;
    left: 0;
    top: 0;
    width: 927px;
    height: 1200px;
  }
  .title {
    font-weight: normal;
  }
  .title-top {
    position: absolute;
    left: 232px;
    top: 296px;
    font-family: "Jost", sans-serif;
    font-weight: 400;
    font-size: 262px;
    line-height: 1;
    color: var(--lemon);
    letter-spacing: -4px;
  }
  .title-mid {
    position: absolute;
    left: 292px;
    top: 530px;
    font-family: "Jost", sans-serif;
    font-style: italic;
    font-weight: 800;
    font-size: 136px;
    line-height: 1;
    color: var(--violet);
    letter-spacing: -3px;
  }
  .title-bottom {
    position: absolute;
    left: 209px;
    top: 651px;
    font-family: "Jost", sans-serif;
    font-weight: 700;
    font-size: 104px;
    line-height: 1;
    color: var(--lemon);
    white-space: nowrap;
    letter-spacing: -1px;
  }
  .author {
    position: absolute;
    left: 426px;
    top: 790px;
    font-family: "Jost", sans-serif;
    font-weight: 400;
    font-size: 23px;
    color: var(--text-light);
  }
</style>
</head>
<body>
  <main class="artboard">
    <p class="proof-label">FRONT COVER_1_1</p>

    <svg class="cover-shape" viewBox="0 0 927 1200" aria-hidden="true">
      <defs>
        <clipPath id="ring-cut">
          <rect x="0" y="0" width="927" height="1125"/>
        </clipPath>
      </defs>
      <path class="cover-panel" fill="var(--ink)"
            d="M178 175 H768 V997 A338 338 0 0 0 178 997 Z"/>
      <path class="cover-arc-ring" fill="var(--violet)" clip-path="url(#ring-cut)" fill-rule="evenodd"
            d="M244 1161 A229 229 0 0 1 702 1161 A229 229 0 0 1 244 1161 Z
               M352 1161 A121 121 0 0 0 594 1161 A121 121 0 0 0 352 1161 Z"/>
    </svg>

    <h1 class="title">
      <span class="title-top">walk</span>
      <span class="title-mid">the</span>
      <span class="title-bottom">HIGH LINE</span>
    </h1>

    <p class="author">By Anders Holmqvist</p>
  </main>
</body>
</html>
```